Calendar Dates Only

Need monthly 2018 calendar showing Australian holidays. Need 2 versions 1 black and white and one with some colour. Also need calendar with week starting on Mondays and also on Sundays. Prefer Indesign versions so text can be changed if necessary. Dates only required which would be A4 landscape format. May also need portrait format.

Colors

```html
<!DOCTYPE html>
<html lang="en">
<head>
<meta charset="utf-8">
<title>2018 Monthly Calendar</title>
<link rel="stylesheet" href="https://fonts.googleapis.com/css2?family=Source+Sans+3:wght@400;600;700&display=swap">
<style>
  :root {
    --backdrop: #d2d2d2;
    --sheet: #ffffff;
    --title: #0d0f5c;
    --weekday: #1a1f96;
    --rule: #c4c4c4;
    --weekend: #b3aeae;
    --holiday: #d9d6d8;
    --date: #333333;
    --holiday-text: #0d0f5c;
  }
  * { box-sizing: border-box; margin: 0; padding: 0; }
  html, body {
    width: 1200px; height: 1139px; overflow: hidden;
    background: var(--backdrop);
    font-family: "Source Sans 3", "Source Sans Pro", sans-serif;
  }
  .month-sheet {
    position: absolute;
    left: 229.6px;
    width: 727.2px;
    height: 513.6px;
    background: var(--sheet);
  }
  .month-sheet--january { top: 38.4px; }
  .month-sheet--february { top: 592px; }
  .month-name {
    position: absolute;
    left: 36.8px; top: 36px;
    font-size: 31px; font-weight: 600;
    color: var(--title); letter-spacing: 0.3px;
  }
  .year {
    position: absolute;
    right: 37.6px; top: 27px;
    font-size: 42px; font-weight: 700;
    color: var(--title);
  }
  .weekday-row {
    position: absolute;
    left: 36.8px; top: 98px;
    width: 653px;
    display: grid;
    grid-template-columns: repeat(7, 1fr);
    text-align: center;
    font-size: 14.5px;
    color: var(--weekday);
  }
  .date-grid {
    position: absolute;
    left: 36.8px; top: 122.4px;
    width: 653px;
    display: grid;
    grid-template-columns: repeat(7, 1fr);
    grid-auto-rows: 71.3px;
  }
  .day {
    position: relative;
    outline: 1px solid var(--rule);
    outline-offset: -0.5px;
    background: var(--sheet);
  }
  .day--blank { outline: none; background: transparent; }
  .day--weekend { background: var(--weekend); outline-color: #d0cccc; }
  .day--holiday { background: var(--holiday); outline-color: #d0cccc; }
  .day-number {
    position: absolute;
    top: 8px; right: 8px;
    font-size: 9px;
    color: var(--date);
  }
  .holiday-name {
    position: absolute;
    top: 13px; left: 3px;
    font-size: 9.5px; font-weight: 600; line-height: 1.3;
    color: var(--holiday-text);
  }
</style>
</head>
<body>

<section class="month-sheet month-sheet--january">
  <h2 class="month-name">JANUARY</h2>
  <div class="year">2018</div>
  <div class="weekday-row">
    <span>MONDAY</span><span>TUESDAY</span><span>WEDNESDAY</span><span>THURSDAY</span><span>FRIDAY</span><span>SATURDAY</span><span>SUNDAY</span>
  </div>
  <div class="date-grid">
    <div class="day day--holiday"><span class="day-number">1</span><span class="holiday-name">New Year’s<br>Day</span></div>
    <div class="day"><span class="day-number">2</span></div>
    <div class="day"><span class="day-number">3</span></div>
    <div class="day"><span class="day-number">4</span></div>
    <div class="day"><span class="day-number">5</span></div>
    <div class="day day--weekend"><span class="day-number">6</span></div>
    <div class="day day--weekend"><span class="day-number">7</span></div>

    <div class="day"><span class="day-number">8</span></div>
    <div class="day"><span class="day-number">9</span></div>
    <div class="day"><span class="day-number">10</span></div>
    <div class="day"><span class="day-number">11</span></div>
    <div class="day"><span class="day-number">12</span></div>
    <div class="day day--weekend"><span class="day-number">13</span></div>
    <div class="day day--weekend"><span class="day-number">14</span></div>

    <div class="day"><span class="day-number">15</span></div>
    <div class="day"><span class="day-number">16</span></div>
    <div class="day"><span class="day-number">17</span></div>
    <div class="day"><span class="day-number">18</span></div>
    <div class="day"><span class="day-number">19</span></div>
    <div class="day day--weekend"><span class="day-number">20</span></div>
    <div class="day day--weekend"><span class="day-number">21</span></div>

    <div class="day"><span class="day-number">22</span></div>
    <div class="day"><span class="day-number">23</span></div>
    <div class="day"><span class="day-number">24</span></div>
    <div class="day"><span class="day-number">25</span></div>
    <div class="day day--holiday"><span class="day-number">26</span><span class="holiday-name">Australia<br>Day</span></div>
    <div class="day day--weekend"><span class="day-number">27</span></div>
    <div class="day day--weekend"><span class="day-number">28</span></div>

    <div class="day"><span class="day-number">29</span></div>
    <div class="day"><span class="day-number">30</span></div>
    <div class="day"><span class="day-number">31</span></div>
  </div>
</section>

<section class="month-sheet month-sheet--february">
  <h2 class="month-name">FEBRUARY</h2>
  <div class="year">2018</div>
  <div class="weekday-row">
    <span>MONDAY</span><span>TUESDAY</span><span>WEDNESDAY</span><span>THURSDAY</span><span>FRIDAY</span><span>SATURDAY</span><span>SUNDAY</span>
  </div>
  <div class="date-grid">
    <div class="day day--blank"></div>
    <div class="day day--blank"></div>
    <div class="day day--blank"></div>
    <div class="day"><span class="day-number">1</span></div>
    <div class="day"><span class="day-number">2</span></div>
    <div class="day day--weekend"><span class="day-number">3</span></div>
    <div class="day day--weekend"><span class="day-number">4</span></div>

    <div class="day"><span class="day-number">5</span></div>
    <div class="day"><span class="day-number">6</span></div>
    <div class="day"><span class="day-number">7</span></div>
    <div class="day"><span class="day-number">8</span></div>
    <div class="day"><span class="day-number">9</span></div>
    <div class="day day--weekend"><span class="day-number">10</span></div>
    <div class="day day--weekend"><span class="day-number">11</span></div>

    <div class="day"><span class="day-number">12</span></div>
    <div class="day"><span class="day-number">13</span></div>
    <div class="day"><span class="day-number">14</span></div>
    <div class="day"><span class="day-number">15</span></div>
    <div class="day"><span class="day-number">16</span></div>
    <div class="day day--weekend"><span class="day-number">17</span></div>
    <div class="day day--weekend"><span class="day-number">18</span></div>

    <div class="day"><span class="day-number">19</span></div>
    <div class="day"><span class="day-number">20</span></div>
    <div class="day"><span class="day-number">21</span></div>
    <div class="day"><span class="day-number">22</span></div>
    <div class="day"><span class="day-number">23</span></div>
    <div class="day day--weekend"><span class="day-number">24</span></div>
    <div class="day day--weekend"><span class="day-number">25</span></div>

    <div class="day"><span class="day-number">26</span></div>
    <div class="day"><span class="day-number">27</span></div>
    <div class="day"><span class="day-number">28</span></div>
  </div>
</section>

</body>
</html>
```